RM Fabworks needs a business card

We are looking for a logo and business card.

Contact Information for Business Card

418 Cobblestone Lane
York, PA 17402
410-555-0173
Rmfabworksco@quorvamail.com

```html
<!DOCTYPE html>
<html lang="en">
<head>
<meta charset="utf-8">
<title>RM Fabworks — Business Card</title>
<link href="https://fonts.googleapis.com/css2?family=EB+Garamond:wght@500&family=Source+Sans+3:wght@400&display=swap" rel="stylesheet">
<style>
  :root {
    --backdrop: #000000;
    --card-white: #ffffff;
    --steel-grey: #5a5a5c;
    --arc-blue: #178fcd;
    --ink: #3a3a3c;
  }
  html, body {
    margin: 0;
    padding: 0;
    width: 1200px;
    height: 1200px;
    overflow: hidden;
    background: var(--backdrop);
  }
  .card {
    position: absolute;
    left: 181px;
    width: 840px;
    height: 480px;
    overflow: hidden;
    background: var(--card-white);
  }
  .card--front { top: 98px; }
  .card--back  { top: 622px; }
  .card__art {
    position: absolute;
    inset: 0;
    width: 840px;
    height: 480px;
  }
  .brand-name {
    position: absolute;
    margin: 0;
    transform: translateX(-50%);
    white-space: nowrap;
    font-family: "EB Garamond", Georgia, serif;
    font-weight: 500;
    font-size: 54px;
    line-height: 1;
    color: var(--ink);
  }
  .card--front .brand-name { left: 368px; top: 196px; }
  .card--back  .brand-name { left: 446px; top: 136px; }
  .contact-list {
    position: absolute;
    left: 492px;
    top: 286px;
    margin: 0;
    padding: 0;
    list-style: none;
    font-family: "Source Sans 3", "Myriad Pro", Arial, sans-serif;
    font-size: 19px;
    color: var(--ink);
  }
  .contact-list__item {
    display: flex;
    align-items: center;
    height: 30px;
    margin-bottom: 30px;
  }
  .contact-list__item:last-child { margin-bottom: 0; }
  .contact-list__icon {
    width: 26px;
    height: 22px;
    margin-right: 16px;
    fill: var(--ink);
    flex: none;
  }
</style>
</head>
<body>

<section class="card card--front">
  <svg class="card__art" viewBox="0 0 1050 600" preserveAspectRatio="none" aria-hidden="true">
    <rect width="1050" height="600" fill="var(--steel-grey)"/>
    <polygon fill="var(--arc-blue)" points="522,0 622,0 1050,408 1050,500 992,448 850,600 804,600 967,423"/>
    <polygon fill="var(--card-white)" points="0,0 522,0 967,423 804,600 0,600"/>
  </svg>
  <h1 class="brand-name">RM Fabworks</h1>
</section>

<section class="card card--back">
  <svg class="card__art" viewBox="0 0 1050 600" preserveAspectRatio="none" aria-hidden="true">
    <rect width="1050" height="600" fill="var(--steel-grey)"/>
    <polygon fill="var(--arc-blue)" points="374,0 454,0 191,284 518,600 422,600 0,192 0,100 149,242"/>
    <polygon fill="var(--card-white)" points="454,0 1050,0 1050,600 518,600 191,284"/>
  </svg>
  <h2 class="brand-name">RM Fabworks</h2>
  <ul class="contact-list">
    <li class="contact-list__item">
      <svg class="contact-list__icon" viewBox="0 0 24 24" aria-hidden="true">
        <path d="M6.6 3.5c.5-.5 1.3-.5 1.8 0l2.1 2.6c.4.5.4 1.2 0 1.7L9.2 9.1c.9 2.1 3.5 4.8 5.7 5.7l1.3-1.3c.5-.4 1.2-.4 1.7 0l2.6 2.1c.5.5.5 1.3 0 1.8l-1.6 1.6c-1 1-2.5 1.2-3.8.6C9.5 17.5 6.5 14.5 4.4 10.9c-.6-1.3-.4-2.8.6-3.8z"/>
        <path d="M14 2.5a7.5 7.5 0 0 1 7.5 7.5h-1.6A5.9 5.9 0 0 0 14 4.1zM14 5.8a4.2 4.2 0 0 1 4.2 4.2h-1.6A2.6 2.6 0 0 0 14 7.4z"/>
      </svg>
      <span>410-555-0173</span>
    </li>
    <li class="contact-list__item">
      <svg class="contact-list__icon" viewBox="0 0 24 24" aria-hidden="true">
        <path d="M12 1.5c-4 0-7 3-7 7 0 5 7 14 7 14s7-9 7-14c0-4-3-7-7-7zm0 9.6a2.6 2.6 0 1 1 0-5.2 2.6 2.6 0 0 1 0 5.2z"/>
      </svg>
      <span>Rmfabworksco@quorvamail.com</span>
    </li>
    <li class="contact-list__item">
      <svg class="contact-list__icon" viewBox="0 0 26 20" aria-hidden="true">
        <path d="M1 3h24v15H1zm2.2 1.6L13 12l9.8-7.4zM2.6 5.6v10.6l6.6-5.6zm20.8 0l-6.6 5 6.6 5.6zM10.4 11.6l-6.8 5h18.8l-6.8-5L13 13.6z"/>
      </svg>
      <span>418 Cobblestone Lane York, PA 17402</span>
    </li>
  </ul>
</section>

</body>
</html>
```